Advanced Therapeutic Massage Therapist

I need a business card advertising my massage services as an advanced therapeutic massage therapist. I offer advanced therapeutic massage, swedish and deep tissue. I want to create a simple, professional and feminine card. I like bright colours and creativity.

I prefer a bold and experimental approach rather than something status-quo. A card to suggest therapeutic healing through dynamic massage. Motifs, shapes or layout which suggest movement and flow.

Target Market(s)

Everybody!

Industry/Entity Type

Health And Wellness

Contact Information for Business Card

The card should include:
My name, logo, services offered and my contact details.

Siobhán Delaney
Massage Therapist

- Swedish - Deep Tissue - Advanced Therapeutic

Phone: (+353) 87 296 1740
Email: regenerate@siobhandelaney-example.com
Website: www.siobhandelany-example.com

Font styles to use
Serif
Sans Serif
Decorative
Script

Colors

Designer to choose colors to be used in the design.

Requirements
Must have
• An example may contain something like this, yet concise:
• "Siobhán Delaney
• Massage Therapist
• - Swedish - Deep Tissue - Advanced Therapeutic"
Nice to have
• This sentence is optional:
• Imagery such as a logo or symbol. I have attached a file containing a logo I had produced however the name is incorrect now as it is "Siobhán" not "Sadie". It could be edited to change it to Siobhán.
• I have sent the file as .psd .jpg. .pdf and .png
• I like when the card conveys energy, movement, pressure points, flow etc.
• I just like the designer to follow their own style and ideas. I like bright colours but must have a lot of a base colour to offset it. I really prefer them to follow their own inspiration. That is my preference.
Should not have
• Pine trees, non-native trees to Britain and Ireland, exotic flowers or animals that are not native to Britain and Ireland.
• I don't like brown as the background colour of the card.
• The cars shouldn't look like a wedding invitation i.e too many floral type designs.

```html
<!DOCTYPE html>
<html lang="en">
<head>
<meta charset="utf-8">
<title>Siobhán Delaney – Massage Therapist business card</title>
<link href="https://fonts.googleapis.com/css2?family=Work+Sans:wght@400;500;600&display=swap" rel="stylesheet">
<style>
  :root {
    --page: #e9e7e3;
    --charcoal: #3b3b3b;
    --ink: #4a4a4a;
    --muted: #6d6d6d;
    --gold: #c9952e;
    --gold-light: #e6c77d;
    --teal: #a9dcd2;
    --white: #ffffff;
  }
  * { box-sizing: border-box; margin: 0; padding: 0; }
  html, body {
    width: 1200px; height: 900px; overflow: hidden;
    background: var(--page);
    font-family: "Work Sans", sans-serif;
  }
  .canvas {
    width: 1200px; height: 900px;
    display: flex; flex-direction: column;
    align-items: center; justify-content: center; gap: 56px;
  }
  .card {
    position: relative;
    width: 640px; height: 366px;
    border-radius: 18px;
    overflow: hidden;
    box-shadow: 0 8px 24px rgba(0,0,0,.18);
  }

  /* Back side */
  .card--back { background: var(--charcoal); color: var(--white); }
  .back-mark {
    position: absolute; left: 0; right: 0; top: 52px;
    display: flex; flex-direction: column; align-items: center;
  }
  .back-mark__disc {
    width: 150px; height: 150px; border-radius: 50%;
    background: radial-gradient(circle, var(--teal) 0%, #8fcfc4 70%, #7fb7a8 100%);
    border: 3px solid var(--gold);
  }
  .back-mark__name {
    margin-top: 18px;
    font-size: 24px; font-weight: 400; letter-spacing: .5px;
    color: var(--white);
  }
  .back-mark__role {
    margin-top: 4px;
    font-size: 13px; letter-spacing: 1.5px; color: #cfcfcf;
  }
  .back-tagline {
    position: absolute; left: 0; right: 0; bottom: 34px;
    text-align: center; font-size: 14px; color: #e8e8e8;
  }

  /* Front side */
  .card--front { background: var(--white); }
  .front-swoosh { position: absolute; inset: 0; }
  .front-mark {
    position: absolute; left: 62px; top: 46px;
    width: 170px; height: 170px; border-radius: 50%;
    background: radial-gradient(circle, #f6e3b0 0%, var(--gold-light) 55%, var(--gold) 100%);
  }
  .details {
    position: absolute; left: 322px; top: 96px;
    color: var(--ink);
  }
  .details__name {
    font-size: 25px; font-weight: 600; color: var(--gold);
    letter-spacing: .5px; text-transform: uppercase; line-height: 1;
  }
  .details__role {
    margin-top: 4px; font-size: 12px; letter-spacing: 1px;
    color: var(--muted); text-transform: uppercase;
  }
  .contact { list-style: none; margin-top: 12px; }
  .contact li {
    display: flex; align-items: center; gap: 10px;
    font-size: 17px; line-height: 1.45;
  }
  .contact svg { width: 12px; height: 12px; flex: none; }
  .divider {
    width: 26px; height: 2px; background: var(--gold);
    margin: 10px 0 12px;
  }
  .services { list-style: none; }
  .services li {
    display: flex; align-items: center; gap: 10px;
    font-size: 19px; line-height: 1.3;
  }
  .services svg { width: 10px; height: 12px; flex: none; }
</style>
</head>
<body>
<main class="canvas">

  <section class="card card--back" aria-label="Card back">
    <div class="back-mark">
      <div class="back-mark__disc"></div>
      <p class="back-mark__name">Siobhán Delaney</p>
      <p class="back-mark__role">massage therapist</p>
    </div>
    <p class="back-tagline">VTCA qualified specialising in advanced therapeutic and deep tissue massage.</p>
  </section>

  <section class="card card--front" aria-label="Card front">
    <svg class="front-swoosh" viewBox="0 0 640 366" preserveAspectRatio="none" aria-hidden="true">
      <path d="M0 238 C150 250 300 300 640 366 L0 366 Z" fill="var(--charcoal)"/>
      <path d="M0 270 C170 292 330 320 600 366" fill="none" stroke="var(--white)" stroke-width="14"/>
      <path d="M0 270 C170 292 330 320 600 366" fill="none" stroke="var(--gold)" stroke-width="6"/>
    </svg>

    <div class="front-mark"></div>

    <div class="details">
      <h1 class="details__name">Siobhán Delaney</h1>
      <p class="details__role">Massage Therapist</p>
      <ul class="contact">
        <li>
          <svg viewBox="0 0 12 12"><path d="M2.5 1 L4.5 1 L5.3 3.6 L4 4.6 C4.7 6 5.9 7.3 7.4 8 L8.4 6.7 L11 7.5 L11 9.5 C11 10.3 10.3 11 9.5 11 C5 11 1 7 1 2.5 C1 1.7 1.7 1 2.5 1 Z" fill="var(--gold)"/></svg>
          (+353) 87 296 1740
        </li>
        <li>
          <svg viewBox="0 0 12 12"><rect x="1" y="2.5" width="10" height="7" rx="1" fill="none" stroke="var(--gold)" stroke-width="1.3"/><path d="M1.5 3 L6 6.5 L10.5 3" fill="none" stroke="var(--gold)" stroke-width="1.3"/></svg>
          siobhanmassage@example.ie
        </li>
      </ul>
      <div class="divider"></div>
      <ul class="services">
        <li><svg viewBox="0 0 10 12"><path d="M2 1 L8 6 L2 11" fill="none" stroke="var(--gold)" stroke-width="1.8"/></svg>Swedish</li>
        <li><svg viewBox="0 0 10 12"><path d="M2 1 L8 6 L2 11" fill="none" stroke="var(--gold)" stroke-width="1.8"/></svg>Deep Tissue</li>
        <li><svg viewBox="0 0 10 12"><path d="M2 1 L8 6 L2 11" fill="none" stroke="var(--gold)" stroke-width="1.8"/></svg>Advanced Therapeutic</li>
      </ul>
    </div>
  </section>

</main>
</body>
</html>
```